Kelvo Marine business card

We sell live saltwater fish and live corals
Kelvo Marine
7 Harlow Ct
Wexbury, NJ. 08041
(555) 555-0147
Contact Information for Business Card
Kelvo Marine
7 Harlow Ct
Wexbury, NJ. 08041
(555) 555-0147
Colors
Designer to choose colors to be used in the design.

```html
<!DOCTYPE html>
<html lang="en">
<head>
<meta charset="utf-8">
<title>Kelvo Marine Business Card</title>
<link rel="stylesheet" href="https://fonts.googleapis.com/css2?family=Barlow:wght@400;600&family=Barlow+Condensed:wght@500&display=swap">
<style>
  :root {
    --backdrop: #e9e4dc;
    --card: #ffffff;
    --navy: #0b4a6f;
    --brand-blue: #1f5e9e;
    --text-blue: #2a62a4;
    --aqua: #3fbfd2;
    --rule: #49c3d4;
  }
  * { margin: 0; padding: 0; box-sizing: border-box; }
  html, body { width: 1200px; height: 828px; overflow: hidden; background: var(--backdrop); }
  .card {
    position: absolute; left: 60px; top: 114px;
    width: 1080px; height: 600px;
    background: var(--card);
    overflow: hidden;
    box-shadow: 0 10px 30px rgba(0,0,0,0.18);
    font-family: "Barlow", Arial, sans-serif;
  }
  .brand-row {
    position: absolute; left: 38px; right: 44px; top: 54px; height: 118px;
    display: flex; align-items: center; gap: 22px;
  }
  .brand-rule { flex: 1; height: 2px; background: var(--rule); }
  .brand-mark {
    width: 112px; height: 112px; border-radius: 50%;
    background: var(--aqua);
  }
  .brand-name {
    font-family: "Barlow Condensed", "Arial Narrow", sans-serif;
    font-weight: 500; font-size: 82px; letter-spacing: 1px;
    color: var(--brand-blue); text-transform: uppercase; line-height: 1;
  }
  .contact {
    position: absolute; right: 44px; top: 364px;
    display: flex; flex-direction: column; align-items: flex-end; gap: 14px;
    color: var(--text-blue); font-size: 29px; letter-spacing: 1px;
  }
  .contact-line { display: flex; align-items: center; gap: 18px; }
  .contact-icon { width: 26px; height: 32px; flex: none; }
  .waves { position: absolute; left: 0; bottom: 0; width: 1080px; height: 600px; }
</style>
</head>
<body>
  <div class="card">
    <div class="brand-row">
      <div class="brand-rule"></div>
      <div class="brand-mark"></div>
      <div class="brand-name">Kelvo Marine</div>
      <div class="brand-rule"></div>
    </div>

    <div class="contact">
      <div class="contact-line">
        <span>7 Harlow Ct Wexbury, NJ. 08041</span>
        <svg class="contact-icon" viewBox="0 0 26 32" aria-hidden="true">
          <path d="M13 1C6.4 1 2 5.8 2 11.6 2 19 13 31 13 31s11-12 11-19.4C24 5.8 19.6 1 13 1z" fill="var(--aqua)"/>
          <circle cx="13" cy="11.5" r="4.2" fill="#fff"/>
        </svg>
      </div>
      <div class="contact-line">
        <span>(555) 555-0147</span>
        <svg class="contact-icon" viewBox="0 0 26 32" aria-hidden="true">
          <rect x="5" y="2" width="16" height="28" rx="3" fill="none" stroke="var(--aqua)" stroke-width="2.6"/>
          <line x1="10" y1="25" x2="16" y2="25" stroke="var(--aqua)" stroke-width="2.4"/>
        </svg>
      </div>
    </div>

    <svg class="waves" viewBox="0 0 1080 600" aria-hidden="true">
      <path d="M0,470 C240,440 470,462 700,512 C860,548 980,552 1080,540 L1080,600 L0,600 Z" fill="var(--navy)"/>
      <path d="M0,500 C250,474 480,492 720,540 C870,568 990,566 1080,556 L1080,562 C990,572 870,575 720,548 C480,502 250,484 0,508 Z" fill="var(--aqua)"/>
      <path d="M460,436 C700,452 900,474 1080,480 L1080,540 C980,552 860,548 700,512 C620,494 540,460 460,436 Z" fill="#fff"/>
      <path d="M470,436 C700,454 900,476 1080,482 L1080,500 C900,498 700,476 470,436 Z" fill="var(--aqua)"/>
    </svg>
  </div>
</body>
</html>
```